New menu design for small coffee shop

I need to design a new menu for a small cafe called The Kettle Wren. I've attached pictures of the old menu to give an idea, I really want a completely new look though. You'll notice that the food, coffee and drinks are currently on separate menus, I want all of this to be on one menu. We want to add images of the food before we print the menu, so ideally you will leave spaces for images of the food.
I'm open to suggestions on paper size and how its folded etc.
I've also attached a word file which has changes for the new menu; some are pricing updates, some are completely different.
Our Facebook page is https://www.socialpage.example/thekettlewren/ might give you an idea of what we're about.
Any other questions let me know.

```html
<!DOCTYPE html>
<html lang="en">
<head>
<meta charset="utf-8">
<title>The Kettle Wren – Menu</title>
<link rel="stylesheet" href="https://fonts.googleapis.com/css2?family=Oswald:wght@500;700&family=Open+Sans:wght@400;600&display=swap">
<style>
  :root {
    --page-bg: #efefef;
    --paper: #ffffff;
    --fold: rgba(0, 0, 0, 0.07);
    --red: #d9261c;
    --ink: #1b1b1b;
    --muted: #555555;
    --bullet: #8bb531;
    --bar: #151515;
    --brand-yellow: #f3e21b;
    --food-light: #e7b06a;
    --food: #c67a36;
    --food-dark: #8e4a1e;
    --salad-green: #6fa83a;
    --salad-plate: #cfe3f0;
  }
  * { box-sizing: border-box; margin: 0; padding: 0; }
  html, body {
    width: 1200px;
    height: 905px;
    overflow: hidden;
    background: var(--page-bg);
  }
  .brochure {
    position: absolute;
    left: 60px;
    top: 170px;
    width: 1080px;
    height: 565px;
    background: var(--paper);
    box-shadow: 0 10px 30px rgba(0, 0, 0, 0.12);
    display: flex;
    overflow: hidden;
  }
  .feature-photo {
    position: absolute;
    left: 0;
    bottom: 0;
    width: 100%;
    height: 290px;
    background: linear-gradient(90deg, var(--food-light), var(--food) 50%, var(--food-dark));
    -webkit-mask-image: linear-gradient(to top, #000 50%, transparent);
            mask-image: linear-gradient(to top, #000 50%, transparent);
  }
  .panel {
    position: relative;
    width: 270px;
    height: 100%;
    border-right: 1px solid var(--fold);
    padding: 34px 22px 0;
  }
  .panel:last-child { border-right: 0; }

  .section-label {
    display: inline-block;
    background: var(--red);
    color: #fff;
    font-family: "Oswald", sans-serif;
    font-weight: 700;
    font-size: 15px;
    letter-spacing: 0.5px;
    padding: 3px 10px;
    margin-bottom: 14px;
  }
  .menu-list { list-style: none; }
  .menu-item {
    display: flex;
    gap: 6px;
    font-family: "Open Sans", sans-serif;
    font-size: 8.5px;
    line-height: 1.35;
    color: var(--muted);
    margin-bottom: 5px;
  }
  .menu-item::before {
    content: "";
    flex: none;
    width: 5px;
    height: 5px;
    margin-top: 3px;
    background: var(--bullet);
  }
  .menu-item .dish { flex: 1; }
  .menu-item .price {
    flex: none;
    color: var(--red);
    font-weight: 600;
  }

  .salad-photo {
    width: 226px;
    height: 170px;
    margin-top: -10px;
    border-radius: 0 0 40% 8%;
    background: radial-gradient(ellipse at 55% 45%, var(--salad-green) 0%, #8fbf5a 45%, var(--salad-plate) 85%);
  }
  .hours {
    margin-top: 40px;
    font-family: "Open Sans", sans-serif;
  }
  .hours-title {
    color: var(--red);
    font-weight: 600;
    font-size: 17px;
    letter-spacing: 0.5px;
  }
  .hours-time {
    color: var(--ink);
    font-weight: 600;
    font-size: 13px;
    margin-top: 2px;
  }

  .brand {
    display: flex;
    align-items: center;
    gap: 10px;
    margin-top: 24px;
  }
  .brand-dot {
    width: 46px;
    height: 46px;
    border-radius: 50%;
    background: var(--brand-yellow);
    flex: none;
  }
  .brand-name {
    font-family: "Oswald", sans-serif;
    font-weight: 500;
    font-size: 22px;
    color: var(--ink);
  }
  .call {
    margin-top: 40px;
    font-family: "Oswald", sans-serif;
  }
  .call-label {
    color: var(--red);
    font-weight: 700;
    font-size: 24px;
    letter-spacing: 0.5px;
  }
  .call-number {
    color: var(--ink);
    font-weight: 700;
    font-size: 30px;
    line-height: 1.1;
  }
  .web-bar {
    position: absolute;
    left: 0;
    right: 0;
    top: 240px;
    height: 34px;
    background: var(--bar);
    color: #fff;
    font-family: "Open Sans", sans-serif;
    font-size: 12px;
    display: flex;
    align-items: center;
    padding-left: 22px;
  }
</style>
</head>
<body>
  <main class="brochure">
    <div class="feature-photo" role="img" aria-label="Photo of golden fried chicken with a dipping bowl and lettuce"></div>

    <section class="panel panel-breakfast">
      <h2 class="section-label">ALL DAY BREAKFAST MENU</h2>
      <ul class="menu-list">
        <li class="menu-item"><span class="dish">Big breakfast: eggs, bacon, sausage, tomato and toast</span><span class="price">$17.5</span></li>
        <li class="menu-item"><span class="dish">Eggs on Turkish toast</span><span class="price">$9.5</span></li>
        <li class="menu-item"><span class="dish">Bacon and eggs on Turkish toast</span><span class="price">$14.5</span></li>
        <li class="menu-item"><span class="dish">Eggs Benedict with ham or salmon</span><span class="price">$16.5</span></li>
        <li class="menu-item"><span class="dish">Veggie brekkie with avocado and feta</span><span class="price">$16.5</span></li>
        <li class="menu-item"><span class="dish">Greek yoghurt with berries and honey</span><span class="price">$12.5</span></li>
        <li class="menu-item"><span class="dish">Waffles with maple syrup and ice cream</span><span class="price">$13.5</span></li>
        <li class="menu-item"><span class="dish">Fruit toast with butter</span><span class="price">$6.5</span></li>
        <li class="menu-item"><span class="dish">Coffee: flat white, latte, cappuccino, long black</span><span class="price">$4.5</span></li>
        <li class="menu-item"><span class="dish">Tea, chai or hot chocolate</span><span class="price">$4.5</span></li>
      </ul>
    </section>

    <section class="panel panel-lunch">
      <h2 class="section-label">LUNCH MENU (FROM 11:30)</h2>
      <ul class="menu-list">
        <li class="menu-item"><span class="dish">B.L.T. on toasted Turkish with aioli</span><span class="price">$12.5</span></li>
        <li class="menu-item"><span class="dish">Chicken wrap with salad and sweet chilli</span><span class="price">$13.5</span></li>
        <li class="menu-item"><span class="dish">Beef burger with cheese, salad and chips</span><span class="price">$17.5</span></li>
        <li class="menu-item"><span class="dish">Caesar salad with bacon and parmesan</span><span class="price">$15.5</span></li>
        <li class="menu-item"><span class="dish">Warm chicken salad with berries and feta</span><span class="price">$16.5</span></li>
        <li class="menu-item"><span class="dish">Quiche of the day with side salad</span><span class="price">$14.5</span></li>
        <li class="menu-item"><span class="dish">Bowl of chips, small or large</span><span class="price">$6.5 / $9.5</span></li>
        <li class="menu-item"><span class="dish">Iced coffee or iced chocolate</span><span class="price">$7.5</span></li>
        <li class="menu-item"><span class="dish">Fresh juices, smoothies and soft drinks</span><span class="price">$6.5</span></li>
      </ul>
    </section>

    <section class="panel panel-hours">
      <div class="salad-photo" role="img" aria-label="Photo of a chicken and berry salad on a light blue plate"></div>
      <div class="hours">
        <p class="hours-title">OPEN HOURS</p>
        <p class="hours-time">7:00AM - 2:00PM</p>
      </div>
    </section>

    <section class="panel panel-cover">
      <div class="brand">
        <span class="brand-dot"></span>
        <span class="brand-name">The Kettle Wren</span>
      </div>
      <div class="call">
        <p class="call-label">CALL NOW</p>
        <p class="call-number">+61 7 3000 0142</p>
      </div>
      <div class="web-bar">www.companywebsite.com</div>
    </section>
  </main>
</body>
</html>
```